Geschäftspapiere für moderne Handwerksfirma
Zielgruppe
Wir sind eine moderne Handwerksfirma im Bereich Elektrotechnik und erneuerbare Energie. Unsere Zielgruppe sind Privatpersonen, Kommunen, Firmen, Landwirtschaften
Aufgabenstellung
Unser Design soll unser Logo, sowie unsere Hauptfarben anthrazit und rot aufweisen.

```html
<!DOCTYPE html>
<html lang="de">
<head>
<meta charset="utf-8">
<title>Kerner Energie – Briefbogen</title>
<link href="https://fonts.googleapis.com/css2?family=Open+Sans:wght@400;700&family=Roboto+Condensed:wght@700&family=Source+Sans+3:wght@300;400&display=swap" rel="stylesheet">
<style>
  :root{
    --backdrop:#c9cdd0;
    --paper:#ffffff;
    --brand-red:#c8001e;
    --anthracite:#939393;
    --ink:#444444;
    --body-grey:#9a9a9a;
    --fold:#b9b9b9;
  }
  html,body{margin:0;padding:0;width:891px;height:1200px;overflow:hidden;background:var(--backdrop);}
  .sheet{position:absolute;left:54px;top:43px;width:782px;height:1114px;background:var(--paper);}
  .band{position:absolute;left:0;width:782px;height:1114px;top:0;pointer-events:none;}
  .abs{position:absolute;margin:0;white-space:nowrap;}
  .brand{left:79px;top:37px;display:flex;align-items:center;gap:10px;}
  .brand-dot{width:62px;height:62px;border-radius:50%;background:var(--brand-red);}
  .brand-name{font-family:"Open Sans",sans-serif;font-weight:700;color:var(--brand-red);font-size:32px;line-height:34px;letter-spacing:.5px;}
  .contact-block{font-family:"Open Sans",sans-serif;font-size:10.5px;line-height:14.5px;}
  .red-bold{color:var(--brand-red);font-weight:700;}
  .contact-line{display:flex;align-items:center;gap:6px;color:var(--ink);}
  .contact-line svg{width:11px;height:11px;fill:var(--brand-red);flex:none;}
  .sender-line{left:79px;top:169px;font-family:"Roboto Condensed",sans-serif;font-weight:700;font-size:8.6px;color:var(--ink);}
  .sender-line .sep{color:var(--brand-red);padding:0 4px;}
  .recipient{left:79px;top:195px;font-family:"Source Sans 3",sans-serif;font-weight:400;font-size:15.5px;line-height:17.3px;color:var(--body-grey);}
  .fold{position:absolute;left:0;height:1px;background:var(--fold);}
  .letter{font-family:"Source Sans 3",sans-serif;font-weight:400;font-size:14.6px;line-height:19px;color:var(--body-grey);left:79px;}
  .footer{font-family:"Open Sans",sans-serif;font-size:10.2px;line-height:14.5px;color:var(--ink);top:1034px;}
</style>
</head>
<body>
<div class="sheet">
  <svg class="band" viewBox="0 0 782 1114" aria-hidden="true">
    <path d="M0 0 H520 Q527 4 530 9 H0 Z" fill="var(--brand-red)"/>
    <path d="M534 0 H782 V20 H548 Q543 8 534 0 Z" fill="var(--anthracite)"/>
    <path d="M0 1094 H248 Q254 1104 262 1114 H0 Z" fill="var(--anthracite)"/>
    <path d="M261 1104 H782 V1114 H267 Q263 1109 261 1104 Z" fill="var(--brand-red)"/>
  </svg>

  <div class="abs brand">
    <div class="brand-dot"></div>
    <div class="brand-name">KERNER<br>ENERGIE</div>
  </div>

  <div class="abs contact-block" style="left:577px;top:55px;">
    <div class="red-bold">Kerner - Energie GmbH</div>
    <div class="red-bold">Lindenweg 12</div>
    <div class="red-bold">87654 Talbrunn</div>
  </div>
  <div class="abs contact-block" style="left:577px;top:115px;">
    <div class="contact-line"><svg viewBox="0 0 24 24"><path d="M6.6 10.8a15 15 0 0 0 6.6 6.6l2.2-2.2c.3-.3.7-.4 1-.2 1.1.4 2.3.6 3.6.6.6 0 1 .4 1 1V20c0 .6-.4 1-1 1A17 17 0 0 1 3 4c0-.6.4-1 1-1h3.5c.6 0 1 .4 1 1 0 1.3.2 2.5.6 3.6.1.3 0 .7-.2 1z"/></svg>+49 (0)8123 456 780</div>
    <div class="contact-line"><svg viewBox="0 0 24 24"><path d="M6 2h12v6H6zM3 9h18v9h-3v4H6v-4H3zm5 6v5h8v-5zM8 4v4h8V4z" fill-rule="evenodd"/></svg>+49 (0)8123 456 781</div>
    <div class="contact-line"><svg viewBox="0 0 24 24"><path d="M2 5h20v2l-10 6L2 7zm0 4l10 6 10-6v10H2z"/></svg>info@kerner-energie.de</div>
  </div>

  <p class="abs sender-line">Kerner - Energie GmbH<span class="sep">|</span>Lindenweg 12<span class="sep">|</span>87654 Talbrunn</p>

  <p class="abs recipient">Herrn<br>MAX MUSTERMANN<br>Muster-Straße 19<br>0815 Hausen</p>

  <div class="fold" style="top:329px;width:26px;"></div>
  <div class="fold" style="top:559px;width:38px;"></div>
  <div class="fold" style="top:724px;width:26px;"></div>

  <p class="abs letter" style="top:340px;">Betreffzeile</p>
  <p class="abs letter" style="top:389px;">Sehr geehrte Damen und Herren,</p>
  <p class="abs letter" style="top:427px;">schön, dass Sie neugierig reinschauen, obwohl hier ja eigentlich noch gar kein richtiger Text<br>steht, sondern nur der sogenannte Blindtext. Dieser Blindtext will Ihnen nämlich sagen: Erstens<br>will er den Texter entschuldigen – tut uns leid, aber es war einfach unmöglich, das Ding gestern<br>Nacht noch exakt auf Länge runterzuschreiben. Das Briefing, Sie wissen schon. Schwieriges<br>Thema. Und die Freundin ist krank, und der Freund wollte in diesen neuen Film. Und dann hat<br>sich der Film so überhaupt nicht gelohnt, sagte er.</p>
  <p class="abs letter" style="top:560px;">Ja, und zweitens haben wir Sie bis hierhin zum Lesen gebracht und wollen damit belegen, dass<br>nicht alle Marktforscher und Kaffeesatzleser recht haben, die sagen, dass unser armer Freund<br>Otto Normalverbraucher und seine hässliche Schwester Lieschen Müller maximal Null Komma<br>gar kein Interesse haben für Texte.</p>
  <p class="abs letter" style="top:655px;">Drittens sollten wir für ein paar Zeilen abschweifen und uns dem Gegenstand unserer Bemüh-<br>ungen zuwenden. Was heißt überhaupt Blindtext? Macht er blind, und wenn ja, wen? Ich denke,<br>das Wörtchen will uns ja auch nur warnend darauf hinweisen, dass viel zu oft nach dem Motto<br>„Augen zu und durch“ verfahren wird bei der verantwortungsvollen Aufgabe, Grauwert zu<br>verteilen.</p>
  <p class="abs letter" style="top:769px;">Erstens will er den Texter entschuldigen – tut uns leid, aber es war einfach unmöglich, das Ding<br>gestern Nacht noch exakt auf Länge runterzuschreiben. Das Briefing, Sie wissen schon. Schwi-<br>eriges Thema. Und die Freundin ist krank, und der Freund wollte in diesen neuen Film. Und dann<br>hat sich der Film so überhaupt nicht gelohnt, sagte er.</p>
  <p class="abs letter" style="top:864px;">Mit freundlichen Grüßen,</p>
  <p class="abs letter" style="top:902px;">Martina Mustermann</p>

  <div class="abs footer" style="left:79px;">
    <div class="red-bold">Kerner - Energie GmbH</div>
    <div class="red-bold">Lindenweg 12</div>
    <div class="red-bold">87654 Talbrunn</div>
  </div>
  <div class="abs footer" style="left:274px;">
    <div class="contact-line"><svg viewBox="0 0 24 24"><path d="M6.6 10.8a15 15 0 0 0 6.6 6.6l2.2-2.2c.3-.3.7-.4 1-.2 1.1.4 2.3.6 3.6.6.6 0 1 .4 1 1V20c0 .6-.4 1-1 1A17 17 0 0 1 3 4c0-.6.4-1 1-1h3.5c.6 0 1 .4 1 1 0 1.3.2 2.5.6 3.6.1.3 0 .7-.2 1z"/></svg>+49 (0)8123 456 780</div>
    <div class="contact-line"><svg viewBox="0 0 24 24"><path d="M6 2h12v6H6zM3 9h18v9h-3v4H6v-4H3zm5 6v5h8v-5zM8 4v4h8V4z" fill-rule="evenodd"/></svg>+49 (0)8123 456 781</div>
    <div class="contact-line"><svg viewBox="0 0 24 24"><path d="M2 5h20v2l-10 6L2 7zm0 4l10 6 10-6v10H2z"/></svg>info@kerner-energie.de</div>
  </div>
  <div class="abs footer" style="left:440px;">
    <div class="red-bold">Amtsgericht Stadt</div>
    <div>ABC 0000XX</div>
    <div>UST-ID DE 000XX</div>
  </div>
  <div class="abs footer" style="left:570px;">
    <div class="red-bold">Bankverbindung ABC</div>
    <div>IBAN DE12 3456 7890 1234 5678</div>
    <div>BIC ABCDEF12345</div>
  </div>
</div>
</body>
</html>
```